Brochure for Community-Based Therapy Company

Will be given out to patients, doctors, case managers. We are redesigning our marketing materials and would like a design for a brochure. We provide therapy to individuals who have been injured in car accidents or on the job. We provide occupational therapy, speech therapy and psychotherapy. We would like the brochure to utilize our corporate ID and color scheme that we are using for our other materials (see attached letterhead and logo).

Stock photos that are used should stay away from images of outpatient or hospital settings, stay away from photos with obvious disabilities (wheelchairs, learning to walk, etc), and nothing that looks like physical therapy, as we don't provide physical therapy only OT, Speech and psychotherapy. Would prefer to not have people wearing masks, as we will use this beyond the pandemic. Also, our staff wears business casual clothing so would prefer photos that the individuals are not wearing scrubs or other medical attire (lab coats, etc).

Target Market(s)

Patients, Physicians/Doctors, Case Managers

Industry/Entity Type

Healthcare

Requirements
Must have
• Prefer a booklet format but doesn't have to be 8.5 inch by 11 inch (can be a little smaller).

```html
<!DOCTYPE html>
<html lang="en">
<head>
<meta charset="utf-8">
<title>Northpoint Recovery Partners – Brochure Spread</title>
<link href="https://fonts.googleapis.com/css2?family=Mulish:wght@300;400;600;700&display=swap" rel="stylesheet">
<style>
  :root{
    --backdrop:#dcdcd8;
    --page:#f4f5f5;
    --sage:#6f8e86;
    --heading:#6d8985;
    --ink:#3b3f3f;
    --rule:#cfd4d4;
    --black:#050505;
    --white:#ffffff;
    --photo-a:#c9ccce;
    --photo-b:#b98e76;
    --photo-c:#8e9196;
  }
  *{box-sizing:border-box;margin:0;padding:0}
  html,body{width:1200px;height:840px;overflow:hidden;background:var(--backdrop)}
  body{font-family:"Mulish",sans-serif;color:var(--ink);position:relative}
  .spread{position:absolute;left:60px;top:10px;width:1080px;height:820px;display:flex;box-shadow:0 10px 30px rgba(0,0,0,.18)}
  .page{position:relative;width:540px;height:820px;background:var(--page)}
  .page--left{background:linear-gradient(90deg,#eef0f0 0%,var(--page) 20%,#f6f7f7 85%,#e3e6e6 100%)}
  .page--right{background:linear-gradient(90deg,#e6e9e9 0%,var(--page) 12%,#f6f7f7 100%)}
  .abs{position:absolute}

  .running-head{left:42px;top:39px;display:flex;align-items:center}
  .running-head__label{border-left:3px solid var(--rule);padding-left:8px;font-size:9px;font-weight:700;line-height:11px;color:var(--sage);text-transform:uppercase;letter-spacing:.02em}
  .running-head__note{margin-left:10px;width:162px;height:21px;border:1px solid var(--rule);border-left:none;font-size:7px;line-height:19px;padding-left:4px;text-transform:uppercase;color:#555}
  .head-rule{left:6px;top:109px;width:534px;height:1px;background:var(--rule)}

  .title{left:42px;top:174px;font-size:29px;font-weight:300;line-height:36px;color:var(--heading)}
  .body-col{top:268px;width:165px;font-size:9.7px;line-height:14.7px;letter-spacing:-.15px;word-spacing:-.4px;text-align:justify;-webkit-hyphens:auto;hyphens:auto;color:var(--ink)}
  .body-col p+p{margin-top:14.7px}
  .body-col--one{left:42px}
  .body-col--two{left:222px}
  .dropcap{float:left;width:5px;height:54px;margin:2px 8px 0 0;background:var(--sage);color:transparent;font-size:1px;overflow:hidden}

  .photo-band{left:463px;top:109px;width:77px;height:628px;background:linear-gradient(180deg,#dfe4e3,#e6eaea)}
  .photo{top:109px;height:213px}
  .photo--left{left:463px;width:77px;background:linear-gradient(100deg,var(--photo-c) 0%,var(--photo-a) 40%,#9a9ca0 100%)}
  .photo--right{left:0;width:530px;background:linear-gradient(100deg,var(--photo-a) 0%,var(--photo-b) 35%,#c9a08a 55%,#4c4f54 75%,#a7a9ac 90%,#d8dadb 100%)}

  .footer-rule{top:776px;height:1px;background:var(--rule)}
  .page-num{top:769px;font-size:24px;font-weight:300;color:#b7bfbf}
  .site{top:782px;font-size:8.5px;color:#333}

  .brand{right:35px;top:38px;display:flex;align-items:center;gap:5px;font-size:10px;font-weight:700;color:var(--sage);text-transform:uppercase;letter-spacing:.03em}
  .brand__dot{width:8px;height:8px;border-radius:50%;background:var(--sage)}

  .serve-bar{left:75px;top:322px;width:455px;height:44px;background:var(--black);color:var(--white);font-size:23px;font-weight:300;line-height:44px;padding-left:10px}
  .serve-intro{left:75px;top:366px;width:195px;height:289px;background:var(--sage);color:var(--white);padding:26px 10px 0 12px;font-size:12px;line-height:16.7px;font-weight:300}
  .serve-intro li{list-style:none;position:relative;padding-left:14px}
  .serve-intro li+li{margin-top:16px}
  .serve-intro li::before{content:"";position:absolute;left:0;top:4px;width:9px;height:9px;border-radius:50%;background:#a9bdb8}

  .diagnoses{left:270px;top:366px;width:260px;height:289px;background:var(--white);padding:10px 6px 0 15px}
  .diagnoses h3,.funding h3{font-weight:300;color:var(--heading)}
  .diagnoses h3{font-size:22px;line-height:30px;margin-bottom:3px;white-space:nowrap}
  .bullets li{list-style:none;position:relative;padding-left:13px;font-size:10.2px;line-height:13.2px;letter-spacing:-.1px;color:#2f3333}
  .bullets li+li{margin-top:3.6px}
  .bullets li::before{content:"›";position:absolute;left:0;top:2px;width:9px;height:9px;border-radius:50%;background:#b4bcbc;color:var(--white);font-size:9px;line-height:8px;text-align:center;font-weight:700}

  .funding{left:75px;top:663px;width:455px;height:71px;background:var(--white);border-top:4px solid #e3e6e6;display:flex;align-items:center;padding-left:17px}
  .funding h3{width:195px;flex:none;font-size:22px;line-height:25px}
  .funding .bullets{padding-left:0;white-space:nowrap}
  .funding .bullets li+li{margin-top:1.5px}
</style>
</head>
<body>
<div class="spread">
  <section class="page page--left">
    <div class="abs running-head">
      <div class="running-head__label">Finding success in the<br>rehabilitative process</div>
      <div class="running-head__note">Relies on certain key factors</div>
    </div>
    <div class="abs head-rule"></div>

    <h2 class="abs title">Why Our Approach to<br>Brain Injury is Unique</h2>

    <div class="abs body-col body-col--one">
      <p><span class="dropcap">I</span>n more traditional therapy settings such as programs using outpatient models, attempts are made to simulate functional activities, combined with more structured tasks, all performed within their clinic environment. However, the inability to generalize learning has been shown to be a reoccurring difficulty for individuals with Traumatic Brain Injury and can often manifest in cognitive inflexibility, which makes carryover of their learned skills to the real world, a challenge.</p>
      <p>Community-based treatment circumvents this difficulty by conducting therapy in the person’s home, school, workplace, or other settings within their community, such as a grocery store or at a post office. Clinicians are therefore able to witness first hand where a task is experiencing success or breaking down and can structure treatment accordingly. This allows for greater natural development of functional skills, with generalization issues no</p>
    </div>
    <div class="abs body-col body-col--two">
      <p>longer an obstacle toward meeting treatment goals.</p>
      <p>At Northpoint Recovery Partners we are committed to helping people recover their cognitive, physical and psychosocial abilities following brain injury through intensive individual treatment which focuses on safety, skill building and increasing independence, community reintegration, and overall life satisfaction. Our treatment approach is two-fold, with emphasis not only on direct restoration of brain functions, but also on helping the individual learn compensatory strategies (e.g., internal mnemonics, organizational systems, self-cuing techniques) or acquire assistive devices (e.g., planners, electronic reminders). Such methods are designed to reduce the effects of real-world disability when there is enduring cognitive impairment, and are most effective when introduced within a person’s own relevant environments.</p>
    </div>

    <div class="abs photo-band"></div>
    <div class="abs photo photo--left" role="img" aria-label="Photo: two people in business suits shaking hands (left portion)"></div>

    <div class="abs footer-rule" style="left:138px;width:326px"></div>
    <div class="abs page-num" style="left:42px">4</div>
    <div class="abs site" style="left:358px">www.northpoint-recovery.com</div>
  </section>

  <section class="page page--right">
    <div class="abs brand"><span class="brand__dot"></span>Northpoint Recovery Partners</div>

    <div class="abs photo photo--right" role="img" aria-label="Photo: two people in business suits shaking hands over a pale hexagon background"></div>

    <h2 class="abs serve-bar">Who We Serve</h2>
    <ul class="abs serve-intro">
      <li>We treat adults and adolescents with a variety of diagnoses. We service home and community locations throughout Southeast and mid-Michigan.</li>
      <li>Our therapists hold a variety of certifications and endorsements including CNRS (Certified Neuro Recovery Specialist), SwallowStim, and VoiceBoost.</li>
    </ul>

    <div class="abs diagnoses">
      <h3>Diagnoses can include:</h3>
      <ul class="bullets">
        <li>Traumatic Brain Injury</li>
        <li>Postconcussional Syndrome</li>
        <li>Spinal Cord Injury</li>
        <li>Post-traumatic Stress Disorder</li>
        <li>Depression</li>
        <li>Anxiety</li>
        <li>Mood Disorders</li>
        <li>Musculoskeletal/Orthopedic injuries (ie. Spinal fractures/pathology, nerve injuries, pain)</li>
        <li>Visual Impairments</li>
        <li>Balance Disorders</li>
        <li>Movement Disorders</li>
        <li>Neuromuscular Pathologies</li>
        <li>Dysphagia</li>
      </ul>
    </div>

    <div class="abs funding">
      <h3>Funding Sources include:</h3>
      <ul class="bullets">
        <li>No-Fault Auto Insurance</li>
        <li>Workers Compensation Insurance</li>
        <li>Some Commercial Health Insurance Carriers</li>
      </ul>
    </div>

    <div class="abs footer-rule" style="left:75px;width:330px"></div>
    <div class="abs site" style="left:75px">www.northpoint-recovery.com</div>
    <div class="abs page-num" style="right:35px">5</div>
  </section>
</div>
</body>
</html>
```